Business Cards + Flyer + Letterhead for Care Recruitment Agency

We are a recruitment agency for the health & care sector. We need designs made for business cards, A5 double-sided flyer, and a letterhead template.

Our branding message is professionalism, care, compassion, expertise. We are experts in recruitment for the care & health industry.

Our logo source files and colours are here - https://www.fileporta.net/sh/qrvn82lopx4kdte/BBBgKy8LMQ27uTnPwZxHcVobsa?dl=0

For the business card, I have attached an example we like. We want a vertical business card design, something very similar to the example given. The design should match our logo in terms of brand colors. On one side should be our logo, our website (www.hollowmere.co.uk) and Care Recruitment Specialists written somewhere visible that fits, between our logo and the website at the bottom. On the other side should be our details.

Details on the front:

Logo with slogan
Care Recruitment Specialists
www.hollowmere.co.uk

Details on the back:

Tobias Orlund
Managing Director

Pellam House, 31-39 Larkfield St, Birmingham, B4 7QD
07612 495371
tobias@hollowmere.co.uk
www.hollowmere.co.uk

Marnie Holloway
Business Development Director

07831 204968
marnie@hollowmere.co.uk
www.hollowmere.co.uk

For the A5 flyer, I have attached some pictures we've used for the website, which could be used for the flyer as well. To get a better idea of our branding, please visit our website - https://hollowmere.co.uk/

The text for the flyer is also attached.

Finally, the letterhead template should be a docx template with our logo and our identifiable branding (the same shapes and matching colours you will come up with for the business cards and flyer).

```html
<!DOCTYPE html>
<html lang="en">
<head>
<meta charset="utf-8">
<title>Hollowmere Letterhead</title>
<link href="https://fonts.googleapis.com/css2?family=Poppins:wght@400;500;600;700&display=swap" rel="stylesheet">
<style>
  :root{
    --navy:#0b2f7a;
    --blue:#1466d8;
    --sky:#3da5f4;
    --pale:#cfe6fb;
    --ink:#2b2b2b;
    --muted:#555;
    --paper:#ffffff;
  }
  *{margin:0;padding:0;box-sizing:border-box}
  html,body{width:849px;height:1200px;overflow:hidden;background:var(--paper)}
  body{font-family:"Poppins",sans-serif;color:var(--ink);position:relative}
  .wave{position:absolute;display:block}
  .wave--top{top:0;right:0}
  .wave--bottom{bottom:0;left:0}

  .brand{position:absolute;left:62px;top:118px;display:flex;align-items:center;gap:14px}
  .brand__dot{width:40px;height:40px;border-radius:50%;background:var(--blue)}
  .brand__name{font-size:36px;font-weight:700;letter-spacing:1px;color:var(--navy);text-transform:uppercase;line-height:1}

  .contact{position:absolute;left:572px;top:128px;list-style:none;font-size:11.5px;color:var(--muted);line-height:16px}
  .contact li{display:flex;align-items:flex-start;gap:14px;margin-bottom:14px}
  .contact svg{flex:0 0 18px;margin-top:2px}

  .rule{position:absolute;left:62px;right:62px;top:300px;height:1px;background:#e2e6ee}

  .recipient{position:absolute;left:62px;top:352px;font-size:12px;line-height:20px}
  .recipient__name{font-size:15px;font-weight:600;color:#111}
  .recipient__role{font-size:11px;margin-bottom:8px}
  .recipient dl{display:grid;grid-template-columns:20px auto;color:var(--muted)}
  .recipient dt{font-weight:600;color:var(--ink)}

  .date{position:absolute;right:62px;top:356px;font-size:15px;font-weight:500}

  .body{position:absolute;left:62px;right:62px;top:532px;font-size:13.6px;line-height:25px;text-align:justify;color:#333}
  .body p{margin-bottom:22px}

  .signoff{position:absolute;right:90px;top:940px;text-align:right}
  .signoff__mark{width:150px;height:52px;border-radius:26px;background:linear-gradient(90deg,#eef2f8,#dde5f1);margin-left:auto;margin-bottom:14px}
  .signoff__name{font-size:14px;font-weight:600;color:#111;line-height:20px}
  .signoff__role{font-size:13px;color:var(--muted)}
</style>
</head>
<body>

<svg class="wave wave--top" width="320" height="110" viewBox="0 0 320 110" aria-hidden="true">
  <path d="M40 0 C110 40 170 20 220 50 C260 74 290 90 320 95 L320 0 Z" fill="var(--pale)"/>
  <path d="M90 0 C150 30 200 10 245 40 C280 62 300 70 320 72 L320 0 Z" fill="var(--sky)"/>
  <path d="M150 0 C200 22 240 10 275 30 C295 42 310 46 320 46 L320 0 Z" fill="var(--blue)"/>
  <path d="M210 0 C245 14 280 8 320 22 L320 0 Z" fill="var(--navy)"/>
</svg>

<header class="brand">
  <span class="brand__dot"></span>
  <span class="brand__name">Hollowmere</span>
</header>

<ul class="contact">
  <li>
    <svg width="18" height="18" viewBox="0 0 24 24"><circle cx="12" cy="12" r="12" fill="#e9eef6"/><path d="M12 5a4.5 4.5 0 0 0-4.5 4.5C7.5 13 12 19 12 19s4.5-6 4.5-9.5A4.5 4.5 0 0 0 12 5zm0 6.2a1.7 1.7 0 1 1 0-3.4 1.7 1.7 0 0 1 0 3.4z" fill="var(--muted)"/></svg>
    <span>Street Address Here<br>Canada, 2222</span>
  </li>
  <li>
    <svg width="18" height="18" viewBox="0 0 24 24"><circle cx="12" cy="12" r="12" fill="#e9eef6"/><path d="M8.6 6.5l1.8-.4 1.2 2.8-1.3 1a7.5 7.5 0 0 0 3.8 3.8l1-1.3 2.8 1.2-.4 1.8c-.1.5-.6.9-1.1.9A10.6 10.6 0 0 1 7.7 7.6c0-.5.4-1 .9-1.1z" fill="var(--muted)"/></svg>
    <span>+000 12345 6789<br>+000 12345 6789</span>
  </li>
  <li>
    <svg width="18" height="18" viewBox="0 0 24 24"><circle cx="12" cy="12" r="12" fill="#e9eef6"/><rect x="6" y="8" width="12" height="8.5" rx="1" fill="none" stroke="var(--muted)" stroke-width="1.4"/><path d="M6.5 8.6L12 13l5.5-4.4" fill="none" stroke="var(--muted)" stroke-width="1.4"/></svg>
    <span>urwebsitename.com<br>urname@email.com</span>
  </li>
</ul>

<div class="rule"></div>

<section class="recipient">
  <div class="recipient__name">Dana Whitfield</div>
  <div class="recipient__role">Chief Director</div>
  <dl>
    <dt>A :</dt><dd>Address, 345 Country Road, Canada - 8989</dd>
    <dt>W :</dt><dd>email@myemail.com, www.myweb.com</dd>
    <dt>P :</dt><dd>+880 - 12345 - 6789</dd>
  </dl>
</section>

<div class="date">Date, 10 December 2022</div>

<main class="body">
  <p>This is a sample letter that has been placed to demonstrate typing remat (Your Company) letterhead design. When positioned properly, it will serve to work in harmony with all other element letterhead. This letterhead design is meant to project an image This letterhead design is mean project an image of professionalism reliability. By using simple aligen we have created a very spacious feeling. The simplicity suggest  rength the spaciousnes contributes aesthetics the layout. These basic qualities along with the (Your Company) look and helps reinforce the (Your Company) brand. letterhead design is meant to project an image  design. When positioned properly, it will serve to work in harmony all the other elements letterhead, sionalism and reliability.</p>
  <p>This letterhead design is based on the (Form of your logo) form (Your Company) logo. Each stationery we have created a very spacious feeling. The simplicity suggests strength the spaciousnes contribute part of the (Form of your logo).</p>
</main>

<div class="signoff">
  <div class="signoff__mark" role="img" aria-label="Handwritten signature of the manager"></div>
  <div class="signoff__name">Owen Prescott</div>
  <div class="signoff__role">Manager</div>
</div>

<svg class="wave wave--bottom" width="849" height="250" viewBox="0 0 849 250" aria-hidden="true">
  <path d="M0 20 C60 40 110 110 190 150 C260 185 330 190 420 205 L420 250 L0 250 Z" fill="var(--pale)"/>
  <path d="M0 60 C70 80 120 140 200 175 C270 205 360 210 460 222 L460 250 L0 250 Z" fill="var(--sky)"/>
  <path d="M0 110 C80 125 140 180 230 205 C300 224 390 228 500 236 L500 250 L0 250 Z" fill="var(--blue)"/>
  <path d="M0 170 C90 180 170 222 280 236 C420 252 600 215 849 200 L849 250 L0 250 Z" fill="var(--navy)"/>
  <path d="M560 250 C640 222 740 205 849 180 L849 250 Z" fill="var(--sky)" opacity=".85"/>
</svg>

</body>
</html>
```